Letterhead and Business card for Construction company

We need a letterhead and business card with our new company logo. We are based in NY. We develop and build properties.

The design should incorporate some unique feature from the logo (shape, font...). it should look like an extension from it.

Design should be clean and elegant, professional, not too busy.

The letterhead should include:
Logo (attached)
Address
Phone
Email

Please find the attached logo images and AI file.

Target Market(s)

Construction industry professionals

Industry/Entity Type

Construction, Development

Font styles to use
Sans Serif

Colors

Designer to choose colors to be used in the design.

Requirements
Must have
• Design should incorporate logo elements, additional assets are welcome. I'd like to see some other shapes / images invorporated too.

```html
<!DOCTYPE html>
<html lang="en">
<head>
<meta charset="utf-8">
<title>Norvale Builders – Letterhead</title>
<link href="https://fonts.googleapis.com/css2?family=Roboto+Slab:wght@400;700&display=swap" rel="stylesheet">
<style>
  :root {
    --backdrop: #dcdcdc;
    --paper: #ffffff;
    --ink: #231f20;
    --accent: #f37f20;
    --faint: #e6e6e6;
    --light-text: #ffffff;
  }
  * { margin: 0; padding: 0; box-sizing: border-box; }
  html, body { width: 1200px; height: 947px; overflow: hidden; }
  body {
    background: var(--backdrop);
    font-family: "Roboto Slab", Georgia, serif;
    position: relative;
  }
  .letterhead {
    position: absolute;
    left: 364px; top: 179px;
    width: 472px; height: 606px;
    background: var(--paper);
    overflow: hidden;
  }
  .brand {
    position: absolute;
    left: 0; right: 0; top: 20px;
    display: flex; flex-direction: column; align-items: center; gap: 4px;
  }
  .brand-mark {
    width: 14px; height: 14px;
    background: var(--accent);
  }
  .brand-name {
    font-weight: 700;
    font-size: 17px;
    letter-spacing: 1px;
    color: var(--ink);
    text-transform: uppercase;
    line-height: 1.1;
    text-align: center;
  }
  .brand-name small {
    display: block;
    font-size: 9px;
    letter-spacing: 2px;
  }
  .watermark {
    position: absolute;
    left: 0; right: 0; top: 252px;
    text-align: center;
    font-weight: 700;
    font-size: 74px;
    letter-spacing: 2px;
    color: var(--faint);
    text-transform: uppercase;
    line-height: 1;
  }
  .footer-rule {
    position: absolute;
    left: 0; right: 0; top: 548px;
    height: 4px;
    background: var(--accent);
  }
  .footer {
    position: absolute;
    left: 0; right: 0; top: 552px; bottom: 0;
    background: var(--ink);
    color: var(--light-text);
    font-size: 10px;
    text-align: center;
  }
  .footer-address {
    padding-top: 7px;
    line-height: 14px;
  }
  .footer-divider {
    width: 378px; height: 1px;
    margin: 3px auto 0;
    background: var(--light-text);
  }
  .footer-contacts {
    margin-top: 3px;
    line-height: 14px;
    white-space: nowrap;
  }
  .footer-contacts .label { color: var(--accent); font-weight: 700; }
  .footer-contacts .sep { margin: 0 6px; }
</style>
</head>
<body>
  <main class="letterhead">
    <header class="brand">
      <span class="brand-mark"></span>
      <div class="brand-name">Norvale<small>Builders</small></div>
    </header>

    <div class="watermark" aria-hidden="true">Norvale</div>

    <div class="footer-rule"></div>
    <footer class="footer">
      <p class="footer-address">Your Address line here, Country Code 0123456</p>
      <div class="footer-divider"></div>
      <p class="footer-contacts">
        <span class="label">P:</span> 044-123 456 789<span class="sep">|</span><span class="label">E:</span> info@webname.com<span class="sep">|</span><span class="label">W:</span>&nbsp; www.websitename.com
      </p>
    </footer>
  </main>
</body>
</html>
```